Postcard to Market Greeting Cards

Need a Postcard to
* Promote a particular human being and his story.
* Market and raise awareness of his art
* Advertise his website where the art can be purchased.

Background:
Davor Kelmandi is a refugee and artist trapped in a refugee camp in Indonesia.
He has committed no crimes. He had to escape his country as a refugee.
He is currently held in detention. The only way out is to be privately sponsored.
This costs a huge amount of money. Davor is working to raise the money needed.
He is young and has lost 5 years being imprisoned. We must work to save him.

He draws everyday and sends the drawings to me. I make them into beautiful hand drawn art cards which we sell at markets, on the internet or via contacts.
He is not allowed to work. Secret drawing is the only way he can make a living.

This postcard is to
* share some of Davor's Story and to give a sense of who he is.
* display his beautiful art cards which are sold for income via his website.
* Prominently display his website address as well as images of the cards.

These postcards will be given out at markets, letterbox dropped, sent to new customers, left in cafes and libraries etc so people will discover Davor's Cards....
By buying the cards...Davor can earn the funds he needs to pay for sponsorship into a free country. Many countries will accept him if he pays for the process.

Therefore...the postcard needs to be filled front and back. No need to leave space for address and postage. This leaves more room for samples of the Greeting Cards.

There is text provided for the front and back of the POSTCARD.
This may be edited and added to as the design process continues.

Images of Davor's Cards have been uploaded for you.
It would be great if these can be beautifully and artistically presented on the postcard. The aim is to attract people to Davor's hand drawn cards motivate people to want to buy them. Not all of the card images need to be used.

There are * black line cards * colour cards. * framed colour art works
so some of each could be promoted on the postcard.

Davor's Story will be included on the back of the card labelled for the Back.
A few words will be clearly and displayed on the front. Labelled fo the front.

The front art can be a single drawing image from Davor OR a collage of many OR
It can contain his image or a few small images. See what you feel works well as there is scope to create a BEAUTIFUL postcard that depicts beautiful CARDS.

There is a quote from Davor to be included on the front.
Can it be written in a handwriting style font to make it look like Davor has written the message himself ?

There are images of Davor to be used on the front and back.
Davor's images have ben taken on dodgy phones and may not be a good quality.
They don't need to be large images and they DON'T need to all be used. There is a selection to choose from.

Davor is in a prison. Maybe there are design elements that might remind of this.
Barbed wire maybe. Fences. The over all feel though is FREEDOM and BEAUTY in the hand drawn art cards and the escape they will provide in the end.

Davor's website to be displayed on the front and back
davorsketch.net

email address on the back
helpdavor2031@mailpost.net

These postcards will encourage buyers to read Davor's Story and want to help.
They will display beautifully hand drawn art cards which people will want to buy.
They will display the website address prominently and in some clever. arty way.

Good luck with it all.
I plan to increase first prize money depending on the designs....
and to offer more than first place depending on the deigns.

Please feel free to ask me any questions at any time.

Good luck and thanks for considering this project.

Neil Farrow

Target Market(s)

Broad human rights supporters who will enjoy seeing a human story and will want to. respond.

Industry/Entity Type

Human Rights

Colors

Designer to choose colors to be used in the design.

Requirements
Must have
• Colourful and imaginative way of displaying the Greeting Cards being marketed by the Postcard. It is a taster and a sampling. They do not need to be arranged in rows or order..better to be creative in displaying the samples of cards. The website has the organised online shop. The postcard is a sampler and should MAKE people want to go to the website to buy the cards. The postcard must share the story of the artist.
• Handwriting font for the quote from the artist to make it look like he has written a personal message.
• Postcard needs to be filled on front and back. No blank space for mailing and address.
Nice to have
• Free and easy arty design. Photograph of the artist placed in some creative way.
Should not have
• Conservative structure. Free and arty is better.
• The postcard needs to be filled on the front and back ! No need to leave the bank area for mailing as it will only be used for marketing and distribution. it won't actually be used for mailing.

```html
<!DOCTYPE html>
<html lang="en">
<head>
<meta charset="utf-8">
<title>Free Davor – Postcard</title>
<link rel="stylesheet" href="https://fonts.googleapis.com/css2?family=Bebas+Neue&family=Gochi+Hand&family=Lato:ital,wght@0,400;0,700;0,900;1,700&family=Oswald:wght@500&display=swap">
<style>
  :root {
    --red: #d52b27;
    --red-deep: #c9211d;
    --ink: #1b1b1b;
    --dark-panel: #1e1e1e;
    --paper: #ffffff;
    --cream: #f3eee8;
    --text: #2a2a2a;
    --muted-grey: #d9d9d9;
    --rule-grey: #a9a9a9;
    --backdrop: #e9e6e2;
  }
  * { box-sizing: border-box; margin: 0; padding: 0; }
  html, body { width: 902px; height: 1200px; overflow: hidden; }
  body {
    background: var(--backdrop);
    font-family: "Lato", Arial, sans-serif;
    color: var(--text);
    position: relative;
  }

  /* ---------- Front of postcard ---------- */
  .postcard-front {
    position: absolute; left: 80px; top: 58px;
    width: 680px; height: 528px;
    background: var(--cream);
    box-shadow: 0 6px 16px rgba(0,0,0,.25);
  }
  .front-dark-panel {
    position: absolute; left: 0; top: 0; width: 308px; height: 528px;
    background: linear-gradient(180deg, #111 0%, var(--dark-panel) 60%, #2a2a2a 100%);
  }
  .artist-portrait {
    position: absolute; left: 41px; top: 24px; width: 224px; height: 224px;
    border-radius: 50%; border: 6px solid var(--paper);
    background: radial-gradient(circle at 50% 40%, #c9a07f 0%, #7a5a48 45%, #d94a9a 80%, #2b2b2b 100%);
  }
  .artist-quote {
    position: absolute; left: 14px; top: 257px; width: 280px;
    font-family: "Gochi Hand", cursive;
    color: var(--paper); font-size: 15.5px; line-height: 16px; text-align: center;
  }
  .quote-signature {
    display: block; text-align: right; margin-top: 10px; padding-right: 18px;
    font-size: 18px; letter-spacing: .5px;
  }
  .front-cta {
    position: absolute; left: 0; top: 414px; width: 340px; height: 134px;
    background: var(--red); padding: 14px 18px 0;
    box-shadow: 0 4px 10px rgba(0,0,0,.3);
  }
  .front-cta-text {
    font-style: italic; font-weight: 700; font-size: 14px; line-height: 18px; color: var(--paper);
  }
  .front-cta-text .help { color: var(--ink); }
  .web-address {
    display: flex; align-items: center; gap: 8px;
    font-weight: 900; color: var(--paper); font-size: 29px; margin-top: 10px;
    white-space: nowrap;
  }
  .web-address svg { width: 18px; height: 18px; flex: none; }

  .front-art-panel {
    position: absolute; left: 308px; top: 0; width: 372px; height: 528px;
    background: linear-gradient(180deg, #f7f3ee 0%, #ece3da 100%);
  }
  .headline-band {
    position: absolute; left: 2px; top: 24px; width: 370px; height: 78px;
    background: var(--red); text-align: center;
    font-family: "Bebas Neue", "Oswald", sans-serif;
    color: var(--paper); font-size: 74px; line-height: 82px; letter-spacing: 1px;
  }
  .support-lines {
    position: absolute; left: 0; top: 116px; width: 372px; text-align: center;
  }
  .support-lines p { font-weight: 700; font-size: 17px; line-height: 23px; color: var(--ink); }
  .support-lines .accent { color: var(--red); font-weight: 900; }
  .support-lines .accent.large { font-size: 24px; line-height: 30px; }

  .polaroid {
    position: absolute; background: var(--paper); padding: 8px 8px 22px;
    box-shadow: 0 4px 10px rgba(0,0,0,.3);
  }
  .polaroid .card-art { width: 100%; height: 100%; }
  .polaroid-hummingbird { left: 41px; top: 218px; width: 145px; height: 152px; transform: rotate(-6deg); }
  .polaroid-oriole { left: 202px; top: 223px; width: 140px; height: 148px; transform: rotate(6deg); }
  .art-hummingbird { background: linear-gradient(150deg, #f4ecea 0%, #efd6d0 55%, #e3b7a8 100%); }
  .art-oriole { background: linear-gradient(150deg, #f7f3ef 0%, #f1e1cf 55%, #d9c7e0 100%); }
  .pin {
    position: absolute; left: 199px; top: 237px; width: 16px; height: 16px; border-radius: 50%;
    background: radial-gradient(circle at 35% 35%, #ff6b62, var(--red-deep) 70%);
    box-shadow: 1px 2px 3px rgba(0,0,0,.4);
  }
  .card-collection {
    position: absolute; left: 75px; top: 386px; width: 226px; height: 104px;
    border: 3px solid var(--paper); box-shadow: 0 3px 8px rgba(0,0,0,.3);
    background: linear-gradient(180deg, #f3c24a 0%, #e9a93b 45%, #b86a2e 100%);
  }

  /* ---------- Back of postcard ---------- */
  .postcard-back {
    position: absolute; left: 148px; top: 621px;
    width: 681px; height: 529px;
    background: var(--paper);
    box-shadow: 0 6px 16px rgba(0,0,0,.25);
  }
  .story {
    position: absolute; left: 21px; top: 20px; width: 334px;
  }
  .story h2 { color: var(--red); font-size: 17px; font-weight: 900; margin-bottom: 6px; }
  .story p { font-size: 10.6px; line-height: 13px; text-align: justify; color: var(--ink); }
  .story-divider { position: absolute; left: 364px; top: 0; width: 3px; height: 318px; background: var(--red); }
  .stamp-box { position: absolute; left: 542px; top: 27px; width: 112px; height: 118px; background: var(--muted-grey); }
  .address-line { position: absolute; left: 411px; width: 244px; height: 1px; background: var(--rule-grey); }

  .offer-strip {
    position: absolute; left: 0; top: 318px; width: 364px; height: 20px;
    background: var(--red); color: var(--paper);
    font-family: "Oswald", sans-serif; font-weight: 500; font-size: 9.6px; line-height: 20px;
    padding-left: 21px; white-space: nowrap;
  }
  .formats-strip {
    position: absolute; left: 0; top: 338px; width: 364px; height: 35px;
    background: var(--ink); color: var(--paper);
    font-style: italic; font-weight: 700; font-size: 11.5px; line-height: 14px;
    padding: 4px 100px 0 21px;
  }
  .availability {
    position: absolute; left: 21px; top: 380px;
    font-style: italic; font-weight: 700; font-size: 11px; color: var(--ink);
  }
  .back-web-band {
    position: absolute; left: 0; top: 400px; width: 368px; height: 50px;
    background: var(--red); padding: 4px 0 0 21px;
  }
  .back-web-band .web-address { margin-top: 0; font-size: 29px; }
  .artist-snapshot {
    position: absolute; left: 285px; top: 316px; width: 82px; height: 84px;
    background: var(--paper); padding: 4px; box-shadow: 0 2px 6px rgba(0,0,0,.35);
  }
  .artist-snapshot div { width: 100%; height: 100%; background: linear-gradient(160deg, #e8b58a 0%, #c7a58f 40%, #f1f1f1 100%); }
</style>
</head>
<body>

<section class="postcard-front">
  <div class="front-dark-panel">
    <div class="artist-portrait" role="img" aria-label="Portrait photo of Davor Kelmandi in a pink shirt"></div>
    <p class="artist-quote">“It's true that my body is prisoner....But my thoughts and my heart are not prisoner..No one can imprison my thoughts and my heart.Because my thoughts and my heart are with those who I love them”
      <span class="quote-signature">Davor Kelmandi.</span>
    </p>
  </div>

  <div class="front-art-panel">
    <div class="headline-band">FREE DAVOR</div>
    <div class="support-lines">
      <p>Buy Davor's Beautiful Art Cards</p>
      <p class="accent">SUPPORT HIM</p>
      <p>Help Davor Pay For His Sponsorship</p>
      <p class="accent large">TO FREEDOM</p>
    </div>
    <div class="polaroid polaroid-hummingbird"><div class="card-art art-hummingbird" role="img" aria-label="Drawing of a hummingbird beside a red flower"></div></div>
    <div class="polaroid polaroid-oriole"><div class="card-art art-oriole" role="img" aria-label="Drawing of a yellow and black bird on a flowering branch"></div></div>
    <div class="pin"></div>
    <div class="card-collection" role="img" aria-label="Photo of a row of hand drawn flower greeting cards"></div>
  </div>

  <div class="front-cta">
    <p class="front-cta-text">Read Davor's Story and Buy His Beautiful Hand Drawn Art Cards. <span class="help">Help Save A Life</span></p>
    <p class="web-address">
      <svg viewBox="0 0 20 20" aria-hidden="true"><g fill="none" stroke="#1b1b1b" stroke-width="1.6"><circle cx="10" cy="10" r="8.5"/><ellipse cx="10" cy="10" rx="3.8" ry="8.5"/><path d="M1.5 10h17M3 5.5h14M3 14.5h14"/></g></svg>
      www.davorsketch.net
    </p>
  </div>
</section>

<section class="postcard-back">
  <article class="story">
    <h2>About Davor Kelmandi</h2>
    <p>Davor Kelmandi, a young Hazara man from Afghanistan, has been illegally held captive in an Indonesian Detention Centre for more than four years. He is a Refugee and prisoner without any crime. The Hazara are a ruthlessly persecuted people. Davor is alone in the world and bravely escaped his country to begin a new free life never expecting to be imprisoned and detained for years. An artist and photographer Davor is now a passionate Human Rights Defender. He refuses to allow his free spirit and creative nature to be dampened or imprisoned. He draws sunny delicate flowers and peaceful fragile birds which sing of freedom. Davor makes his art to maintain his sanity and to encourage all who struggle for freedom to reach out and grab it with both hands. He draws daily to remind himself that what is important inside him can never be locked away. Davor wastes no time being a prisoner. He is too busy dreaming free. His art expresses that.</p>
    <p>The only escape for Davor is to be sponsored to a free country. It costs many thousands to be sponsored. Davor needs your help. He's not asking for favours or charity. He is working daily for this.</p>
    <p>Davor's daily drawings have become individual greeting cards and his beautiful, unique cards are now for sale to fund his freedom. Buy Davor's Greeting Cards so he can pay his own way to freedom.</p>
  </article>
  <div class="story-divider"></div>
  <div class="stamp-box"></div>
  <div class="address-line" style="top:262px"></div>
  <div class="address-line" style="top:307px"></div>
  <div class="address-line" style="top:351px"></div>

  <div class="offer-strip">INDIVIDUAL CARDS. SETS OF CARDS. STUNNING FRAMED ART WORKS.</div>
  <div class="formats-strip">Beautiful black line drawing cards and full colour cards available.</div>
  <p class="availability">Davor's Cards, Art and Designs are available from</p>
  <div class="back-web-band">
    <p class="web-address">
      <svg viewBox="0 0 20 20" aria-hidden="true"><g fill="none" stroke="#1b1b1b" stroke-width="1.6"><circle cx="10" cy="10" r="8.5"/><ellipse cx="10" cy="10" rx="3.8" ry="8.5"/><path d="M1.5 10h17M3 5.5h14M3 14.5h14"/></g></svg>
      www.davorsketch.net
    </p>
  </div>
  <div class="artist-snapshot"><div role="img" aria-label="Small photo of Davor Kelmandi in a white shirt"></div></div>
</section>

</body>
</html>
```